Harwood Cleaning – Website Redesign (Clean, Modern, Trust-Focused)

Harwood Cleaning — Homepage Redesign Brief

Project Goal

We need a complete redesign of the homepage for our cleaning business, Harwood Cleaning.
The goal is a clean, modern, trust-building homepage that works equally well for:
• Residential clients
• Commercial clients

The page should feel polished, reliable, easy to navigate, and completely free from clutter, gimmicks, or corporate-sounding fluff.

About Us (Context)

Harwood Cleaning has operated in Sale, Victoria for over 30 years.
Our brand is built on:
• Reliability
• Convenience
• Long-term trust
• Straightforward, no-nonsense communication

We do not want to look like a large franchise, and we do not want to look cute or playful.
The design must feel modern, practical, confident, and professional.

What We Need Designed — Homepage Only

1. Hero Section

A clean, modern hero area with:
• A simple image or clean background (no clutter, no heavy overlays).
Images from our current site may be helpful, or you may source alternatives.
• Headline suggestion (designer may refine):
“30+ Years of Commercial and Residential Cleaning in Sale”
• Sub-headline suggestion:
“Trusted by locals for three decades.”
• Primary CTA button: Get a Quote

2. Trust-Building Logos

Positioned directly beneath the hero:
• Small, neat logos of organisations we work with
(RTB, Brightway, Eastvale District Health, KPL, etc.)
• A clean Rateline Reviews block (stars + review count)
• Must be compact, tidy, evenly spaced — not loud or oversized

3. Trust Block / Problem–Solution Copy

This section introduces why hiring cleaners can be stressful and why reliability matters.

Headline example:
“Call the cleaners you can count on.”

We have existing copy for this section.
Please present it in a minimal, breathable, modern layout that is easy to scan.

4. Stats / Counters Section

Three sharp, structured stat boxes:
• 92+ Recurring Clients
• 4,150+ Visits Per Year
• 265+ Pre-Sale / Exit Cleans

These should look clean and understated — not oversized or gimmicky.

5. Values Section

A short section featuring our core values:
• Be Real
• Do It Right
• Have Fun
• Make It Easy

Designer has flexibility with layout.
(Sections 5 and 6 may swap depending on what flows better.)

6. Services Preview

A simple grid or row with links to our main services:
• Commercial Cleaning
• Residential Cleaning
• Window Cleaning
• Steam Cleaning

Small icons or photos are fine — but no clip art or cartoon-style graphics.

7. Footer

A very clean, simple footer with contact details.
No clutter, no heavy visual styling.

Style Requirements

Overall Tone
• Clean
• Modern
• Minimal
• Trust-driven
• Easy to read and navigate

Do NOT use
• Clip art
• Cute or playful icons
• Flowers, sparkles, “feminine” cleaning imagery
• Heavy or overly bold corporate fonts
• Busy backgrounds
• Long paragraphs of text

Reference Material

Current Website (for copy + structure only)

https://harwoodcleaning.example.au

Rough Sketchly Mock-Up (layout inspiration only)

(We will upload this separately. It’s not a final design — just a loose concept for spacing/flow.)

Logo

Please use the new Harwood Cleaning logo (uploaded in files) or a placeholder if needed. Attached is a potential for a new logo or site colours not wedded to the idea though.

What the Homepage Should Communicate

Within seconds, a visitor should understand that:
• We are established
• We are local
• We are reliable
• We make cleaning easy
• Getting a quote is quick and simple

The homepage should feel effortless, trustworthy, and modern.

Deliverable

A complete homepage design layout suitable for WordPress.
Figma, Adobe XD, or a similar design tool is fine.

Target Market(s)

Residential and commercial clients in Sale, Victoria and surrounding Gippsland region. Typical clients include busy households, office managers, receptionists, medical centres, community organisations, local businesses, and real estate/property professionals. Clients value reliability, simplicity, and stress-free long-term cleaning support.

Industry/Entity Type

Cleaning services (Residential & Commercial)

Font styles to use
Sans Serif

Requirements
Must have
• • Clean, modern, minimal layout • A trust-driven design that highlights proof (logos, stats, reviews) near the top • Clear hierarchy and no clutter • A strong hero section with simple messaging and a clear CTA • Trust logos + Rateline Reviews block directly under the hero • Structured stats/counters section • Values section (Be Real, Do It Right, Have Fun, Make It Easy) • Services preview (Commercial, Residential, Window, Steam/Carpet) • Clean footer with contact details • Use our new Harwood Cleaning logo (or placeholder if needed) • Easy-to-read typography and spacing • Must feel like a local, real cleaning business — not a franchise
Nice to have
• • An option with centred hero text and an option with left-aligned text • Option to preview hero section with or without a quote form • Subtle use of the navy + gold palette (not heavy or corporate) • Soft, minimal background images (not busy city skylines) • Subtle section dividers or whitespace breaks to improve flow • Slightly rounded card corners for a friendly but still modern feel
Should not have
• • No clip-art, cartoon mops, sparkles, bubbles, or generic cleaning icons • No overly bold, blocky, or corporate fonts • No “mega-city” skylines (we are a regional/rural business) • No heavy overlays, dark gradients, or cluttered hero images • No long paragraphs or dense text blocks • No template-style designs that look generic or AI-generated • No overly feminine, overly masculine, or overly playful designs • No neon colors or high-saturation palettes

```html
<!DOCTYPE html>
<html lang="en">
<head>
<meta charset="utf-8">
<title>Harwood Cleaning – Homepage</title>
<link href="https://fonts.googleapis.com/css2?family=Montserrat:wght@400;500;600;700;800&display=swap" rel="stylesheet">
<style>
:root{
  --navy:#152a4c;
  --navy-deep:#0f203b;
  --gold:#c8a83c;
  --gold-soft:#d7bb59;
  --ink:#1c2433;
  --muted:#6b7280;
  --line:#e3e5ea;
  --pale:#eceef2;
  --white:#ffffff;
  --footer-text:#dfe4ec;
}
*{margin:0;padding:0;box-sizing:border-box}
html,body{width:1200px;height:4976px;overflow:hidden}
body{font-family:"Montserrat",sans-serif;color:var(--ink);background:var(--white);position:relative}
.abs{position:absolute}
.btn{display:inline-block;font-family:"Montserrat",sans-serif;font-weight:700;font-size:11px;letter-spacing:.06em;text-transform:uppercase;padding:12px 26px;border-radius:3px;background:var(--gold);color:var(--navy-deep)}
.btn-navy{background:var(--navy);color:var(--white)}
.btn-outline{background:transparent;border:1px solid var(--white);color:var(--white)}
.h-section{font-weight:800;text-transform:uppercase;color:var(--navy);font-size:34px;line-height:1.15}
.small{font-size:12px;line-height:1.6;color:var(--muted)}
.ph{display:block}

/* header + hero */
.hero{left:0;top:0;width:1200px;height:700px;background:linear-gradient(160deg,#5f87b8 0%,#9fb8d3 35%,#b9c6d4 60%,#7f93ad 100%)}
.header{left:0;top:0;width:1200px;height:68px;background:rgba(15,32,59,.55);display:flex;align-items:center;padding:0 112px}
.logo{font-weight:800;font-size:20px;color:var(--white);letter-spacing:.02em;display:flex;align-items:center;gap:8px}
.logo .mark{width:12px;height:12px;background:var(--gold)}
.nav{margin-left:auto;display:flex;gap:34px;font-size:11px;color:var(--white);font-weight:500;align-items:center}
.nav .btn{padding:9px 18px;font-size:10px}
.hero-copy{left:120px;top:150px;width:720px;color:var(--white)}
.hero-copy h1{font-weight:800;font-size:44px;line-height:1.2;text-transform:uppercase}
.hero-copy p{margin:22px 0 24px;font-size:13px}
.stats{left:112px;top:652px;width:976px;height:102px;background:var(--gold);border-radius:4px;display:flex;align-items:center;justify-content:space-around}
.stat{display:flex;align-items:center;gap:14px;color:var(--white);font-size:12px;font-weight:600}
.stat .num{width:70px;height:70px;border-radius:50%;border:2px solid rgba(255,255,255,.7);display:flex;align-items:center;justify-content:center;font-size:17px;font-weight:800}

/* trust block */
.trust-img{left:120px;top:820px;width:420px;height:440px;background:radial-gradient(circle at 45% 40%,#c7d2dc 0%,#e9edf1 55%,#ffffff 100%)}
.trust-copy{left:580px;top:860px;width:480px}
.trust-copy p{font-size:12px;line-height:1.7;color:var(--muted);margin-top:14px}
.trust-copy p b{color:var(--ink)}

/* services */
.services{left:0;top:1288px;width:1200px;height:412px;background:var(--navy);color:var(--white);text-align:center}
.services h2{color:var(--white);margin-top:70px}
.services .lead{font-size:13px;margin-top:10px;color:#d8dde6}
.svc-row{display:flex;justify-content:center;gap:40px;margin-top:50px}
.svc{width:220px}
.svc .icon{width:64px;height:64px;background:var(--gold);margin:0 auto 18px;display:flex;align-items:center;justify-content:center;border-radius:3px}
.svc h3{font-size:12px;font-weight:700;text-transform:uppercase;margin-bottom:8px}
.svc p{font-size:11px;line-height:1.6;color:#c6cdd9}

/* what we clean */
.clean-head{left:112px;top:1760px;width:600px}
.clean-head p{margin-top:10px;width:440px}
.card{background:var(--white);border-radius:6px;box-shadow:0 6px 22px rgba(21,42,76,.12);overflow:hidden}
.card .ph{height:170px}
.card .body{padding:16px 18px}
.card h4{font-size:12px;font-weight:700;text-transform:uppercase;color:var(--navy);margin-bottom:8px}
.card-feature{left:112px;top:1870px;width:330px;height:350px;background:linear-gradient(180deg,#4c5561 0%,#2b323c 100%);border-radius:6px;color:var(--white);padding:170px 22px 0}
.card-feature h4{font-size:13px;font-weight:800;text-transform:uppercase;margin-bottom:10px}
.card-feature p{font-size:10.5px;line-height:1.6;color:#e1e4ea}
.card-feature .more{margin-top:12px;font-size:10px;font-weight:700;color:var(--gold-soft);text-transform:uppercase;text-decoration:underline}

/* about */
.about{left:0;top:2288px;width:1200px;height:360px;background:var(--gold)}
.about-img{left:0;top:2288px;width:560px;height:360px;background:linear-gradient(135deg,#2f6db1 0%,#d24e7a 50%,#f1c04b 100%)}
.about-copy{left:600px;top:2360px;width:480px;color:var(--white)}
.about-copy h2{color:var(--white);font-size:32px}
.about-copy p{font-size:11px;line-height:1.7;margin:16px 0 22px}
.about-copy .btn{margin-right:12px}

/* values */
.values-head{left:0;top:2710px;width:1200px;text-align:center}
.values-head p{margin-top:8px}
.values{left:112px;top:2830px;width:976px;height:210px}
.values .divider{position:absolute;left:488px;top:0;width:1px;height:200px;background:var(--line)}
.val{position:absolute;width:420px;display:flex;gap:20px}
.val .n{flex:none;width:64px;height:64px;border-radius:4px;background:#eef0f4;color:var(--navy);font-weight:800;font-size:22px;display:flex;align-items:center;justify-content:center}
.val .n.gold{background:#f6efd8;color:var(--gold)}
.val h5{font-size:13px;font-weight:800;text-transform:uppercase;color:var(--navy);margin:6px 0 6px}
.val p{font-size:10.5px;line-height:1.6;color:var(--muted)}

/* contact */
.contact{left:0;top:3160px;width:1200px;height:420px;background:linear-gradient(100deg,#3a4655 0%,#6c7886 40%,#9aa6b2 70%,#c5ccd4 100%)}
.contact-copy{left:440px;top:3240px;width:360px;color:var(--white)}
.contact-copy h2{color:var(--white);font-size:34px;text-align:center}
.contact-copy .q{font-size:11px;margin:10px 0 16px;text-align:center}
.contact-copy ul{list-style:none;font-size:11px}
.contact-copy li{display:flex;gap:10px;align-items:center;margin-bottom:8px}
.contact-copy li span{width:11px;height:11px;border:1px solid var(--white)}
.contact-copy .btn{margin-top:14px;padding:10px 30px}

/* reviews */
.reviews-head{left:112px;top:3700px;width:360px}
.reviews-head p{margin-top:12px}
.dots{display:flex;gap:7px}
.dots i{width:7px;height:7px;border-radius:50%;background:#c9ccd3}
.dots i.on{background:var(--navy)}
.review{padding:30px 30px;border-radius:4px}
.review .who{display:flex;align-items:center;gap:14px;margin-bottom:18px}
.review .av{width:52px;height:52px;border-radius:50%;background:#c9cfd8}
.review .name{font-size:13px;font-weight:800;text-transform:uppercase}
.review .role{font-size:10px}
.review p{font-size:11px;line-height:1.7}
.review .date{font-size:10px;margin-top:16px;font-weight:600}
.review-gold{left:520px;top:3640px;width:370px;height:360px;background:var(--gold);color:var(--navy-deep)}
.review-white{left:920px;top:3680px;width:320px;height:300px;background:var(--white);box-shadow:0 6px 22px rgba(21,42,76,.12)}
.quote-mark{position:absolute;right:30px;top:34px;font-size:60px;font-weight:800;line-height:1;color:rgba(15,32,59,.35)}

/* blogs */
.blogs{left:0;top:4060px;width:1200px;height:512px;background:var(--pale)}
.blogs-head{left:0;top:4110px;width:1200px;text-align:center}
.blogs-head p{margin-top:8px}
.blog .ph{height:150px}
.blog .body{padding:16px 18px}
.blog .date{font-size:10px;color:var(--gold);font-weight:600;margin-bottom:6px}
.blog h4{font-size:13px;font-weight:800;text-transform:uppercase;color:var(--navy);margin-bottom:8px}
.blog p{font-size:10.5px;line-height:1.6;color:var(--muted)}

/* footer */
.footer{left:0;top:4572px;width:1200px;height:404px;background:var(--navy)}
.foot-logo{left:0;top:4612px;width:1200px;text-align:center;font-weight:800;font-size:22px;letter-spacing:.02em;color:var(--white)}
.foot-links{left:112px;top:4700px;list-style:none;font-size:11px;line-height:2.05;color:var(--white)}
.foot-contact{left:380px;top:4700px;font-size:11px;line-height:2.05;color:var(--footer-text)}
.foot-contact b{font-weight:700;color:var(--white)}
.foot-map{left:800px;top:4700px;font-size:11px;color:var(--white)}
.foot-map .ph{margin-top:10px;width:150px;height:100px;background:linear-gradient(135deg,#e8ebef,#cfd5dc);border-radius:3px}
.foot-badge{left:985px;top:4690px;width:110px;height:110px;border-radius:50%;border:3px solid var(--white);background:var(--navy-deep);display:flex;align-items:center;justify-content:center}
.foot-badge span{width:70px;height:70px;border-radius:50%;border:1px solid var(--gold)}
.socials{left:0;top:4872px;width:1200px;display:flex;justify-content:center;gap:12px}
.socials i{width:26px;height:26px;border-radius:50%;background:var(--gold)}
.copyright{left:0;top:4930px;width:1200px;text-align:center;font-size:9px;letter-spacing:.1em;color:#b7c0cf}
</style>
</head>
<body>

<!-- Hero -->
<div class="abs hero ph" role="img" aria-label="Upward view of a glass office tower against a blue sky"></div>
<header class="abs header">
  <div class="logo"><span class="mark"></span>HARWOOD CLEANING</div>
  <nav class="nav">
    <span>Commercial</span><span>Residential</span><span>Window Cleaning</span><span>Steam Cleaning</span><span>Areas</span>
    <span class="btn">Contact</span>
  </nav>
</header>
<div class="abs hero-copy">
  <h1>30+ Years of Commercial<br>&amp; Residential Cleaning<br>in Sale</h1>
  <p>Trusted by locals for three decades</p>
  <span class="btn">Get a Quote</span>
</div>
<div class="abs stats">
  <div class="stat"><span class="num">92+</span>Recurring Clients</div>
  <div class="stat"><span class="num">4,150+</span>Visits Per Year</div>
  <div class="stat"><span class="num">265+</span>Pre-Sale / Exit Cleans</div>
</div>

<!-- Trust block -->
<div class="abs trust-img ph" role="img" aria-label="Smiling cleaner holding a caddy of cleaning supplies"></div>
<div class="abs trust-copy">
  <h2 class="h-section">Call the cleaners you<br>can count on</h2>
  <p>When you need help cleaning, the last thing you want is more stress.</p>
  <p><b>Too often, that's exactly what happens.</b><br>Cleaners don't show up, jobs get rushed or half-done. And you're left <b>wondering why you didn't just do it yourself.</b></p>
  <p>You shouldn't have to remind anyone whether the job will be done right.</p>
  <p>You should be able to book it, forget it, and trust it's looked after.</p>
  <p><b>Trusted by locals for 30+ years</b> to deliver reliable, long-term cleaning – the kind you never have to second-guess.</p>
  <p style="margin-top:22px"><span class="btn">Contact Us</span></p>
</div>

<!-- Services -->
<section class="abs services">
  <h2 class="h-section">Our Cleaning Services</h2>
  <p class="lead">Professional, reliable cleaning for homes and businesses across Sale</p>
  <div class="svc-row">
    <div class="svc">
      <div class="icon"><svg width="30" height="30" viewBox="0 0 30 30" fill="none" stroke="#fff" stroke-width="2"><rect x="6" y="4" width="18" height="23"/><path d="M10 9h3M17 9h3M10 14h3M17 14h3M10 19h3M17 19h3"/></svg></div>
      <h3>Commercial Cleaning</h3>
      <p>Reliable scheduled cleaning for offices, healthcare, retail and more.</p>
    </div>
    <div class="svc">
      <div class="icon"><svg width="30" height="30" viewBox="0 0 30 30" fill="none" stroke="#fff" stroke-width="2"><path d="M4 15 15 5l11 10M7 13v13h16V13"/><rect x="12" y="18" width="6" height="8"/></svg></div>
      <h3>Residential Cleaning</h3>
      <p>Consistent, no-nonsense home cleaning from a trusted local team.</p>
    </div>
    <div class="svc">
      <div class="icon"><svg width="30" height="30" viewBox="0 0 30 30" fill="none" stroke="#fff" stroke-width="2"><rect x="5" y="4" width="20" height="22"/><path d="M15 4v22M5 15h20"/></svg></div>
      <h3>Window Cleaning</h3>
      <p>Streak-free window cleaning for homes, shops and commercial sites.</p>
    </div>
    <div class="svc">
      <div class="icon"><svg width="30" height="30" viewBox="0 0 30 30" fill="none" stroke="#fff" stroke-width="2"><path d="M15 4c5 7 8 11 8 15a8 8 0 0 1-16 0c0-4 3-8 8-15z"/></svg></div>
      <h3>Steam Cleaning</h3>
      <p>Deep steam cleaning for carpets, rugs and high-traffic areas.</p>
    </div>
  </div>
</section>

<!-- What we clean -->
<div class="abs clean-head">
  <h2 class="h-section">What We Clean</h2>
  <p class="small">Practical cleaning for the places you live and work, done properly every visit, by a local team you can rely on.</p>
</div>
<div class="abs card-feature" role="img" aria-label="Modern office interior with desks and glass partitions">
  <h4>Commercial</h4>
  <p>From GP clinics and local health services to offices and shop fronts, we keep your workplace clean.</p>
  <div class="more">Learn more</div>
</div>
<div class="abs card" style="left:472px;top:1870px;width:290px;height:350px">
  <div class="ph" role="img" aria-label="Bright, tidy living room" style="background:linear-gradient(135deg,#d9cfc1,#f2ece3)"></div>
  <div class="body"><h4>Recurring Residential</h4><p class="small">Weekly or fortnightly home cleaning from the same friendly team, so you always know who is coming.</p></div>
</div>
<div class="abs card" style="left:790px;top:1870px;width:290px;height:350px">
  <div class="ph" role="img" aria-label="Freshly cleaned kitchen and dining area" style="background:linear-gradient(135deg,#e6e2dc,#f7f5f1)"></div>
  <div class="body"><h4>One-Time &amp; Specialty Cleaning</h4><p class="small">Exit cleans, pre-sale cleans and one-off deep cleans when you need a property ready fast.</p></div>
</div>
<div class="abs card" style="left:1108px;top:1870px;width:290px;height:350px">
  <div class="ph" role="img" aria-label="Clean glass windows" style="background:linear-gradient(135deg,#c9d5df,#eef2f5)"></div>
  <div class="body"><h4>Glass Cleaning</h4><p class="small">Clear glass inside and out.</p></div>
</div>

<!-- About -->
<div class="abs about"></div>
<div class="abs about-img ph" role="img" aria-label="Gloved hands holding a basket of colourful cleaning products"></div>
<div class="abs about-copy">
  <h2 class="h-section">About Harwood Cleaning</h2>
  <p>Harwood Cleaning has been cleaning homes and businesses across Sale for over 30 years. We are a local team built on reliability, convenience and long-term trust, with straightforward communication and no fuss. Our clients stay with us because we turn up, do the job right and make cleaning easy.</p>
  <span class="btn btn-navy">Start Here</span><span class="btn btn-outline">Contact Us</span>
</div>

<!-- Values -->
<div class="abs values-head">
  <h2 class="h-section">What We Stand For</h2>
  <p class="small">The simple values guide every clean, every client and every interaction.</p>
</div>
<div class="abs values">
  <div class="divider"></div>
  <div class="val" style="left:0;top:0"><div class="n">1</div><div><h5>Be Real</h5><p>We communicate honestly, show up as promised and keep things straightforward.</p></div></div>
  <div class="val" style="left:0;top:110px"><div class="n gold">2</div><div><h5>Do It Right</h5><p>We take pride in the details and consistent work, done to a high standard.</p></div></div>
  <div class="val" style="left:556px;top:0"><div class="n gold">3</div><div><h5>Have Fun</h5><p>We enjoy what we do and bring a positive, respectful attitude to every job.</p></div></div>
  <div class="val" style="left:556px;top:110px"><div class="n">4</div><div><h5>Make It Easy</h5><p>We keep the process simple, friendly and stress-free for our clients.</p></div></div>
</div>
<div class="abs" style="left:0;top:3070px;width:1200px;text-align:center"><span class="btn">Get a Quote</span></div>

<!-- Contact -->
<div class="abs contact ph" role="img" aria-label="Cleaner wiping a desk in a bright office"></div>
<div class="abs contact-copy">
  <h2 class="h-section">Contact Us</h2>
  <p class="q">What type of cleaning service are you enquiring about?</p>
  <ul>
    <li><span></span>End of lease cleaning</li>
    <li><span></span>Recurring home cleaning</li>
    <li><span></span>Commercial cleaning</li>
    <li><span></span>Window cleaning</li>
    <li><span></span>Carpet and upholstery</li>
    <li><span></span>Other</li>
  </ul>
  <span class="btn">Next</span>
</div>

<!-- Reviews -->
<div class="abs reviews-head">
  <h2 class="h-section">What Clients Say</h2>
  <p class="small">Real feedback from homes and businesses we look after across Sale and the surrounding region.</p>
  <div class="dots" style="margin-top:24px"><i class="on"></i><i></i><i></i></div>
</div>
<div class="abs review review-gold">
  <div class="quote-mark">”</div>
  <div class="who"><div class="av" role="img" aria-label="Client portrait"></div><div><div class="name">Dale M.</div><div class="role">Designer</div></div></div>
  <p>Reliable, thorough and easy to deal with. The team always turns up on time and our office has never looked better. I would recommend them to anyone needing regular cleaning.</p>
  <p class="date">15 May 2025 at 09:00</p>
</div>
<div class="abs review review-white">
  <div class="who"><div class="av" role="img" aria-label="Client portrait"></div><div><div class="name" style="color:var(--navy)">Dale M.</div><div class="role">Designer</div></div></div>
  <p style="color:var(--muted)">Friendly, careful and always consistent. Booking is simple and the results speak for themselves.</p>
  <p class="date" style="color:var(--muted)">15 May 2025 at 09:00</p>
</div>

<!-- Blogs -->
<div class="abs blogs"></div>
<div class="abs blogs-head">
  <h2 class="h-section">Latest Blogs</h2>
  <p class="small">Practical cleaning tips and local news from the Harwood team.</p>
</div>
<div class="abs card blog" style="left:120px;top:4200px;width:300px;height:310px">
  <div class="ph" role="img" aria-label="Cleaner mopping an office floor" style="background:linear-gradient(135deg,#b9c3cf,#e4e8ec)"></div>
  <div class="body"><div class="date">15 May 2025 at 09:00</div><h4>Lorem ipsum dolor sit amet</h4><p>Lorem ipsum dolor sit amet, consectetur adipiscing elit, sed do eiusmod tempor.</p></div>
</div>
<div class="abs card blog" style="left:450px;top:4200px;width:300px;height:310px">
  <div class="ph" role="img" aria-label="Cleaner vacuuming a carpet" style="background:linear-gradient(135deg,#c7c1b8,#ece8e2)"></div>
  <div class="body"><div class="date">15 May 2025 at 09:00</div><h4>Lorem ipsum dolor sit amet</h4><p>Lorem ipsum dolor sit amet, consectetur adipiscing elit, sed do eiusmod tempor.</p></div>
</div>
<div class="abs card blog" style="left:780px;top:4200px;width:300px;height:310px">
  <div class="ph" role="img" aria-label="Cleaner mopping a bright living room" style="background:linear-gradient(135deg,#a9c0d6,#e6edf3)"></div>
  <div class="body"><div class="date">15 May 2025 at 09:00</div><h4>Lorem ipsum dolor sit amet</h4><p>Lorem ipsum dolor sit amet, consectetur adipiscing elit, sed do eiusmod tempor.</p></div>
</div>
<div class="abs dots" style="left:576px;top:4535px"><i class="on"></i><i></i><i></i></div>

<!-- Footer -->
<footer class="abs footer"></footer>
<div class="abs foot-logo">HARWOOD CLEANING</div>
<ul class="abs foot-links">
  <li>Commercial</li><li>Residential</li><li>Window Cleaning</li><li>Steam Cleaning</li><li>Contact</li><li>Areas</li>
</ul>
<div class="abs foot-contact">
  <div><b>Address:</b> 12 Example Street, Sale VIC 3850</div>
  <div><b>ABN:</b> 00 000 000 000</div>
  <div><b>Email:</b> hello@harwoodcleaning.example.au</div>
  <div><b>Phone:</b> 03 5100 0000</div>
</div>
<div class="abs foot-map">
  <div>Service Areas</div>
  <div class="ph" role="img" aria-label="Map of the Sale service area"></div>
</div>
<div class="abs foot-badge" role="img" aria-label="Thirty years of service badge"><span></span></div>
<div class="abs socials"><i></i><i></i><i></i><i></i></div>
<div class="abs copyright">COPYRIGHT © 2025. ALL RIGHTS RESERVED</div>

</body>
</html>
```